Uncoded front page web design for wedding and event planning company

Hi.

I am launching a wedding and event planning company called Silver Fern Gatherings and need a professional and appealing web design.

So, let me explain my company. I am based in Swindon in Wiltshire but the company will plan weddings and events in Oxfordshire, Wiltshire, Berkshire and London.

We will plan weddings, birthdays, conferences, product launches, fashion shows and conventions but the main focus of the website at this stage should be the weddings with all the other occasions being covered under a single 'events' heading.

My contact details for the website should be:
Marion Blake
marion@silverferngatherings.co.uk
01632 960457 / 07700 900583

I'd like the website to feel clean, bright and elegant and be set against a white or off-white background. My logo is purple and I'd therefore like some purple incorporated into the design although feel free to use a more muted purple as my one might be a little bright? I'm also considering whether it would look nice paired with a little of the colour gold - maybe as a font colour in places?? I'll leave you to figure that one out as your design eye will be better than mine but for your reference below is my purple colour and my suggested gold one....

My purple colour is Pantone 2592 C but feel free to use others
My suggested gold I'm looking at is Pantone 14-1041 TCX

I would like to incorporate a Facebook feed in the front page if possible, if it looks right. I'd also like to include a variety of pictures as well so I've included a few in a Dropbox folder which is linked below. Please don't feel obliged to use them all by any means (there's loads!) but you've got a few there to play with. If you find any other royalty free images you'd rather use please go ahead but on the understanding I can have them afterwards!

My logo can be retrieved via this Dropbox link...
You'll notice there are 2 styles of placement. Please feel free to use either to fit in with your design...
https://www.filedrawer-example.com/sh/qk7pa2mwx9rn4lt/BBBKzq8ohPnvve4S03LoPjvb?dl=0

The wedding images I have are in this Dropbox folder...
https://www.filedrawer-example.com/sh/m8wd6rzp2lo4ye1/BBB4kqrXv8nWd7S05JmOgtlp?dl=0

Other than that, it's over to you.... I can't wait to receive your designs :-)

Ooh....finally just to say, as I receive designs in I think I'll notice aspects that I like and don't like and if I feel they'll be useful for other designers, I'll update my brief below. Thanks

BRIEF UPDATE:
Someone asked if I had a tag-line. Could you use "Creating exquisite occasions today for amazing memories tomorrow"

I realise I hadn't explained what I'd like included on my home page so here's some notes to consider....

A welcome to section for me to start narrative about us and our services which has a button that links to our 'about us' page and 'services' page for further information.

A section that nicely illustrates what services we offer whether that be with icons or pictures.

A section with some photos in that would link to our gallery

A section that shows some customer reviews and blog entries that would link to my reviews page and blog to read more.

And finally a contact us section with my details, social media links and site map.

***
I also need to draw attention to where in the UK my services cover. I was therefore thinking perhaps we could use a picture to demonstrate this where it highlights Wiltshire, Oxfordshire, Berkshire and London on a map thereby demonstrating our areas covered. I have found several English county maps when searching on Google but I'm not sure how to highlight the areas I cover (or dull out the areas I don't) so if you have any ideas on this, I'd really like it incorporated. Thanks. (by the way, for those of you not familiar with English counties, the ones I cover are often abbreviated to Wilts, Oxon, Berks, London, so if you find a suitable map with those names on rather than the full names, you'll know what they are!)

I've found an image of the county map which might work well. I was wondering whether we might somehow grey out the counties I don't cover and just keep the ones I do as mentioned above and then crop it into perhaps a shadowed circle? I've attached a screenshot to the brief.
Updates

I've decided on the tag-line "Creating exquisite occasions today for amazing memories tomorrow" so if that could be included somewhere that would be great. I also need to draw attention to where in the UK my services cover. I was therefore thinking perhaps we could use a picture to demonstrate this where it highlights Wiltshire, Oxfordshire, Berkshire and London on a map thereby demonstrating our areas covered. I have found several English county maps when searching on Google but I'm not sure how to highlight the areas I cover (or dull out the areas I don't) so if you have any ideas on this, I'd really like it incorporated. Thanks. Added Wednesday, June 24, 2015

Target Market(s)

Predominately women aged 25-55

Industry/Entity Type

Wedding Planner

Number of Pages Required

1 page

Font styles to use
Sans Serif
Script

Requirements
Nice to have
• I'd like to see how the colour theme of purple and perhaps a little gold (maybe as a font colour) look against a white background. I've mentioned the Pantone colours in the brief above.
• I've attached a screenshot of a webpage with gold writing in and fonts that I like. Perhaps it could give you inspiration?
Should not have
• I really don't like the font QUILLORA so please done use that.

```html
<!DOCTYPE html>
<html lang="en">
<head>
<meta charset="utf-8">
<title>Silver Fern Gatherings</title>
<link rel="stylesheet" href="https://fonts.googleapis.com/css2?family=Great+Vibes&family=Open+Sans:ital,wght@0,300;0,400;0,600;0,700;1,400&display=swap">
<style>
:root{
  --purple:#8d1e8f;
  --purple-soft:#a23aa6;
  --gold:#d4a35a;
  --gold-btn:#d6a862;
  --ink:#555;
  --ink-light:#777;
  --off-white:#f7f7f7;
  --footer:#e9e7ea;
  --white:#fff;
}
*{margin:0;padding:0;box-sizing:border-box}
html,body{width:705px;height:1200px;overflow:hidden}
body{position:relative;background:var(--white);font-family:"Open Sans",sans-serif;color:var(--ink)}
.abs{position:absolute}
.script{font-family:"Great Vibes",cursive;font-weight:400}

/* header */
.site-header{left:0;top:0;width:705px;height:50px;background:linear-gradient(#fff 60%,#f1eef2)}
.brand{left:113px;top:12px;display:flex;align-items:center;gap:6px;color:var(--purple);font-size:13px;font-weight:600;letter-spacing:.3px}
.brand-dot{width:18px;height:18px;border-radius:50%;background:var(--purple)}
.main-nav{left:309px;top:18px;display:flex;gap:0;font-size:11.5px;font-weight:300;color:#555}
.main-nav span{display:inline-block}
.main-nav .sep{margin:0 12px;color:#999}
.main-nav .active{color:var(--purple);font-weight:600}

/* hero */
.hero{left:0;top:50px;width:705px;height:239px;background:linear-gradient(100deg,#e9ece6 0%,#f3f1ee 20%,#c9c2bb 45%,#ece8e4 65%,#4a3a33 80%,#f4f2f0 90%,#ddd 100%)}
.hero-box{left:119px;top:92px;width:289px;height:122px;background:rgba(22,22,40,.82);text-align:center;color:#fff}
.hero-box h1{font-family:"Great Vibes",cursive;font-weight:400;font-size:24px;line-height:21px;margin-top:10px}
.hero-box p{font-size:6px;line-height:7.5px;margin:10px 18px 0;color:#ddd}
.btn-outline{display:inline-block;margin-top:9px;border:1.5px solid var(--gold);color:var(--gold);font-size:7.5px;font-weight:600;padding:4px 6px;letter-spacing:.3px}
.hero-tab{left:0;top:262px;width:705px;height:27px}
.dot{top:273px;width:8px;height:8px;border-radius:50%;background:#e6d1ad}
.dot.on{background:var(--purple)}

/* gallery strip */
.gallery{left:0;top:297px;width:705px;height:75px;display:flex;gap:2px}
.gallery div{flex:1}

/* welcome */
.welcome{left:0;top:380px;width:705px;height:141px;background:var(--off-white);text-align:center}
.welcome h2{font-size:30px;color:#555;margin-top:10px;line-height:36px}
.welcome h2 em{font-style:normal;color:var(--gold)}
.welcome p{font-size:7.8px;line-height:13px;margin:6px auto 0;width:420px;color:#555}
.btn{display:inline-block;background:var(--gold-btn);color:#fff;font-size:7.5px;font-weight:700;letter-spacing:.3px;padding:0 10px;height:21px;line-height:21px}
.welcome .btn{margin-top:14px;width:64px;padding:0}

/* section titles */
.section-title{width:705px;left:0;text-align:center;color:var(--gold);font-size:26px}
.rule{left:306px;width:93px;height:6px}

/* services */
.services-intro{left:190px;top:574px;width:325px;text-align:center;font-size:6.2px;font-style:italic;line-height:7.5px;color:#555}
.service{top:603px;width:120px;text-align:center}
.service .photo{width:90px;height:90px;border-radius:50%;margin:0 auto;border:4px solid #e4dbd0}
.service h3{font-family:"Great Vibes",cursive;font-weight:400;color:var(--purple);font-size:15px;margin-top:9px;line-height:16px}
.service p{font-size:6px;line-height:7.2px;color:#777;margin-top:4px}

/* blog */
.blog{left:0;top:795px;width:705px;height:265px;background:var(--off-white)}
.card{top:855px;width:115px;height:157px;background:#fff;border-top:2px solid #e7c99a}
.card .photo{margin:3px 3px 0;height:74px;position:relative}
.badge{position:absolute;left:-3px;top:20px;width:29px;height:30px;background:var(--purple);color:#fff;text-align:center}
.badge b{display:block;font-size:13px;font-weight:400;line-height:15px;margin-top:2px}
.badge small{display:block;font-size:4px;line-height:6px}
.card h4{font-family:"Great Vibes",cursive;font-weight:400;color:#333;font-size:9.5px;line-height:8.5px;margin:8px 4px 0}
.card .meta{font-size:4.4px;color:var(--gold);margin:4px 4px 0;font-style:italic}
.card p{font-size:4.6px;line-height:6px;color:#666;margin:2px 4px 0}
.card .more{position:absolute;right:6px;bottom:11px;font-size:4.8px;color:var(--purple);display:flex;align-items:center;gap:2px}
.card .more i{width:4px;height:4px;border-radius:50%;background:var(--purple);display:inline-block}

/* footer */
.footer-line{left:0;top:1069px;width:705px;height:2px;background:var(--gold)}
.site-footer{left:0;top:1071px;width:705px;height:129px;background:var(--footer)}
.f-col{top:1086px;width:115px}
.f-col h5{font-size:6.6px;font-weight:700;color:var(--purple);letter-spacing:.2px;margin-bottom:10px}
.f-brand{display:flex;align-items:center;gap:4px;color:var(--purple);font-size:9px;font-weight:600;margin:4px 0 8px}
.f-brand i{width:12px;height:12px;border-radius:50%;background:var(--purple);display:inline-block}
.f-col p{font-size:5.3px;line-height:7.6px;color:#444;text-align:justify}
.f-links div{font-size:5.8px;color:#444;line-height:12.6px}
.info-row{display:flex;gap:8px;font-size:5.6px;color:#444;line-height:8px;margin-bottom:9px}
.info-row svg{flex:none;margin-top:1px}
.socials{display:flex;gap:6px;margin:8px 0 0 16px}
.socials span{width:12px;height:12px;border-radius:2px;background:var(--purple-soft)}
.copy{margin-top:14px;border-top:1px solid #c9c5ca;padding-top:5px;text-align:center;font-size:5px;line-height:7.5px;color:#444}
</style>
</head>
<body>

<header class="abs site-header">
  <div class="abs brand"><span class="brand-dot"></span>Silver Fern Gatherings</div>
  <nav class="abs main-nav">
    <span class="active">Home</span><span class="sep">/</span>
    <span>About</span><span class="sep">/</span>
    <span>Services</span><span class="sep">/</span>
    <span>Blog</span><span class="sep">/</span>
    <span>Contact</span>
  </nav>
</header>

<section class="abs hero" role="img" aria-label="Bride in a white gown signing the register beside white flowers"></section>
<div class="abs hero-box">
  <h1>Creating exquisite occasions today<br>for amazing memories tomorrow</h1>
  <p>Etiamursus leo vel metus. Nulla facilisi. Aec eros. Vestibulum ante ipsu primis in faucibus orci luctus et trices posuere cubilia Suspendisse sollici. Scelerisque</p>
  <span class="btn-outline">LEARN MORE</span>
</div>
<svg class="abs hero-tab" viewBox="0 0 705 27" aria-hidden="true"><polygon points="221,0 484,0 491,27 214,27" fill="#fff"/></svg>
<span class="abs dot" style="left:333px"></span>
<span class="abs dot on" style="left:348px"></span>
<span class="abs dot" style="left:363px"></span>

<div class="abs gallery">
  <div role="img" aria-label="Hands holding wedding rings" style="background:linear-gradient(#c9ced8,#e4dcd6)"></div>
  <div role="img" aria-label="Groom holding bridal bouquet" style="background:linear-gradient(#d9d6d2,#3b3b3f)"></div>
  <div role="img" aria-label="Back of a lace wedding dress" style="background:linear-gradient(#e8d7c9,#b88f74)"></div>
  <div role="img" aria-label="Glasses on a reception table" style="background:linear-gradient(#b39a7b,#e6e1db)"></div>
  <div role="img" aria-label="Set table with white plates" style="background:linear-gradient(#e5e2dc,#a7a294)"></div>
  <div role="img" aria-label="Rose bouquet and gold rings" style="background:linear-gradient(#f5f1ea,#e8c8c0)"></div>
  <div role="img" aria-label="Flower girl in a garden" style="background:linear-gradient(#7f8f59,#ddd2c6)"></div>
  <div role="img" aria-label="Catering staff serving plates" style="background:linear-gradient(#e8e0dc,#9a8472)"></div>
  <div role="img" aria-label="Evening banquet with purple flowers" style="background:linear-gradient(#51406e,#b2a3c8)"></div>
</div>

<section class="abs welcome">
  <h2 class="script">Welcome to <em>Silver Fern</em></h2>
  <p>Lorem ipsum dolor sit amet, consectetur adipiscing elit, sed do eiusmod tempor incididunt ut labore et dolore magna aliqua. Ut enim ad minim veniam, quis nostrud exercitation ullamco laboris nisi ut aliquip commodo consequat. Duis aute irure dolor in reprehenderit in voluptate velit esse cillum dolore eu cupidatat non prdeser</p>
  <span class="btn">A BOUT US</span>
</section>

<h2 class="abs section-title script" style="top:526px">Our services</h2>
<svg class="abs rule" style="top:559px" viewBox="0 0 93 6" aria-hidden="true"><line x1="0" y1="3" x2="36" y2="3" stroke="#ccc"/><line x1="57" y1="3" x2="93" y2="3" stroke="#ccc"/><circle cx="46.5" cy="3" r="2" fill="none" stroke="#bbb"/></svg>
<p class="abs services-intro">Lorem ipsum dolor sit amet, consectetur adipisicing elit, sed do eiusmod tempor incididunt ut labore et dolore magna aliqua. Ut enim ad minim veniam, quis nostrud exercitation ullamco</p>

<div class="abs service" style="left:96px">
  <div class="photo" role="img" aria-label="Ring placed on a hand" style="background:radial-gradient(circle,#c6dc6a,#8cbf3b)"></div>
  <h3>Wedding Planning</h3>
  <p>Lorem ipsum dolor sit amet,<br>consectetur adipiscing elit. Non,<br>dignissimos nihil unde.</p>
</div>
<div class="abs service" style="left:227px">
  <div class="photo" role="img" aria-label="Children celebrating at a party" style="background:radial-gradient(circle,#8fb3d9,#6a8a4a)"></div>
  <h3>Birthdays</h3>
  <p>Lorem ipsum dolor sit amet,<br>consectetur adipiscing elit. Non,<br>dignissimos nihil unde.</p>
</div>
<div class="abs service" style="left:357px">
  <div class="photo" role="img" aria-label="Model in a red dress on a runway" style="background:radial-gradient(circle,#d8452a,#6a1410)"></div>
  <h3>Fashion shows</h3>
  <p>Lorem ipsum dolor sit amet,<br>consectetur adipiscing elit. Non,<br>dignissimos nihil unde.</p>
</div>
<div class="abs service" style="left:487px">
  <div class="photo" role="img" aria-label="Audience at a conference presentation" style="background:radial-gradient(circle,#e9ecef,#6d7079)"></div>
  <h3>Conferences</h3>
  <p>Lorem ipsum dolor sit amet,<br>consectetur adipiscing elit. Non,<br>dignissimos nihil unde.</p>
</div>
<span class="abs btn" style="left:321px;top:757px;width:64px;padding:0;text-align:center">KNOW MORE</span>

<section class="abs blog"></section>
<h2 class="abs section-title script" style="top:803px">Our blog</h2>
<svg class="abs rule" style="top:836px" viewBox="0 0 93 6" aria-hidden="true"><line x1="0" y1="3" x2="36" y2="3" stroke="#ccc"/><line x1="57" y1="3" x2="93" y2="3" stroke="#ccc"/><circle cx="46.5" cy="3" r="2" fill="none" stroke="#bbb"/></svg>

<article class="abs card" style="left:109px">
  <div class="photo" role="img" aria-label="Plated food being served" style="background:linear-gradient(#dcd8d2,#a38c78)"><div class="badge"><b>09</b><small>JUN, 2015</small></div></div>
  <h4>Lorem ipsum dolor sit amet, title consectetur</h4>
  <div class="meta">By Admin / 0 Comment / Blog</div>
  <p>Lorem ipsum dolor sit amet, ut labore et dolore magna et sed aliqua et enim.</p>
  <span class="more"><i></i>Read More</span>
</article>
<article class="abs card" style="left:233px">
  <div class="photo" role="img" aria-label="Roses with gold wedding rings" style="background:linear-gradient(#f6f3ee,#ecd2c4)"><div class="badge"><b>11</b><small>MAR, 2015</small></div></div>
  <h4>Lorem ipsum dolor sit amet, title consectetur</h4>
  <div class="meta">By Admin / 0 Comment / Blog</div>
  <p>Lorem ipsum dolor sit amet, consectetur adipiscing tempor et enim.</p>
  <span class="more"><i></i>Read More</span>
</article>
<article class="abs card" style="left:358px">
  <div class="photo" role="img" aria-label="Coral pink roses" style="background:linear-gradient(#f08070,#d0504a)"><div class="badge"><b>12</b><small>JAN, 2015</small></div></div>
  <h4>Lorem ipsum dolor sit amet, title consectetur</h4>
  <div class="meta">By Admin / 0 Comment / Blog</div>
  <p>Lorem ipsum dolor sit amet, consectetur adipiscing tempor incididunt</p>
  <span class="more"><i></i>Read More</span>
</article>
<article class="abs card" style="left:482px">
  <div class="photo" role="img" aria-label="Bouquet beside a teacup" style="background:linear-gradient(#9fa6a8,#e9ecef)"><div class="badge"><b>01</b><small>JAN, 2015</small></div></div>
  <h4>Lorem ipsum dolor sit amet, title consectetur</h4>
  <div class="meta">By Admin / 0 Comment / Blog</div>
  <p>dolor sit amet, consectetur adipiscing tempor incididunt ut labore et dolore magna et sed</p>
  <span class="more"><i></i>Read More</span>
</article>
<span class="abs btn" style="left:321px;top:1025px;width:64px;padding:0;text-align:center">GO TO &nbsp;BLOG</span>

<div class="abs footer-line"></div>
<footer class="abs site-footer"></footer>

<div class="abs f-col" style="left:115px">
  <h5>ABOUT US</h5>
  <div class="f-brand"><i></i>Silver Fern Gatherings</div>
  <p>Lorem ipsum dolor sit amet, consectetur adipisicing elit. Quam culpa, hic autem itaque. Natus, ducimus quis. Iusto quaerat harum atque earum illum reprehenderit nisi quasi odit, optio iure officiis eaque.</p>
</div>

<div class="abs f-col f-links" style="left:233px">
  <h5>CATEGORIES</h5>
  <div style="margin-top:14px">Home</div>
  <div>About us</div>
  <div>Our services</div>
  <div>Our blog</div>
  <div>Contact</div>
</div>

<div class="abs f-col" style="left:357px;width:120px">
  <h5>INFO</h5>
  <div class="info-row"><svg width="7" height="7" viewBox="0 0 10 10"><circle cx="5" cy="5" r="4" fill="none" stroke="#a23aa6" stroke-width="1.4"/><path d="M5 2.5V5h2" stroke="#a23aa6" stroke-width="1.2" fill="none"/></svg><span>Monday – Friday (9:00am – 5:00pm)</span></div>
  <div class="info-row"><svg width="7" height="8" viewBox="0 0 10 12"><path d="M5 11C2 7 1 5.5 1 4a4 4 0 0 1 8 0c0 1.5-1 3-4 7z" fill="#a23aa6"/><circle cx="5" cy="4" r="1.4" fill="#e9e7ea"/></svg><span>PO 1232 Your Road, &nbsp;M09 77 R<br>City - country</span></div>
  <div class="info-row"><svg width="7" height="7" viewBox="0 0 10 10"><path d="M1 5L9 1 6 9 5 6z" fill="#a23aa6"/></svg><span>marion@silverferngatherings.co.uk</span></div>
  <div class="info-row"><svg width="7" height="7" viewBox="0 0 10 10"><path d="M2 1l2 2-1 1.5c.8 1.4 1.7 2.3 3 3L7.5 6l2 2-1.5 1.5C4.5 9 1 5.5.5 2.5z" fill="#a23aa6"/></svg><span>01632 960457 &nbsp;/ &nbsp;07700 900583</span></div>
</div>

<div class="abs f-col" style="left:483px;width:110px">
  <h5>SOCIAL</h5>
  <div class="socials" aria-label="Social media links"><span></span><span></span><span></span><span></span><span></span></div>
  <div class="copy">Copyright ©2015 Silver Fern Gatherings,<br>All rights reserved</div>
</div>

</body>
</html>
```